Business Card Design

our business is purchasing, rehabbing and flipping homes. Design a house in the palm of a hand. This card is for a new company based in Georgia. So we buy homes that have been foreclosed, short sales,abandond, old homes and vacant homes.
We help improve the communities that we work in. We would like to see designs that use a black background with green accent and other colors that blend and don't take away from the logo and other important information.

Industry/Entity Type

Business

Contact Information for Business Card

Mavenbrook Holdings
Turning Old Doors Into New Starts
2738 Fenwick Lane
Duluth GA 30418
Office: 678-555-0192
mavenbrookholdingsllc.example

```html
<!DOCTYPE html>
<html lang="en">
<head>
<meta charset="utf-8">
<title>Mavenbrook Holdings – Business Card</title>
<link rel="stylesheet" href="https://fonts.googleapis.com/css2?family=Questrial&family=Poppins:wght@600&display=swap">
<style>
  :root {
    --page: #ffffff;
    --card: #000000;
    --frame: #3ad6e4;
    --accent: #a8f03c;
  }
  * { margin: 0; padding: 0; box-sizing: border-box; }
  html, body { width: 1200px; height: 702px; overflow: hidden; background: var(--page); }
  .card {
    position: absolute; left: 22px; top: 22px; width: 1158px; height: 658px;
    background: var(--card); color: var(--accent);
    font-family: "Questrial", sans-serif;
  }
  .card-frame {
    position: absolute; left: 20px; top: 22px; width: 1118px; height: 618px;
    border: 3px solid var(--frame);
  }
  .text { position: absolute; line-height: 1; white-space: nowrap; }
  .brand-name { left: 98px; top: 110px; font-size: 62px; }
  .brand-mark {
    position: absolute; left: 876px; top: 140px; width: 74px; height: 74px;
    background: var(--accent);
  }
  .tagline-lead { left: 347px; top: 262px; font-size: 53px; }
  .tagline-strong {
    left: 506px; top: 334px; font-size: 80px;
    font-family: "Poppins", sans-serif; font-weight: 600; text-transform: uppercase;
  }
  .tagline-end { left: 870px; top: 418px; font-size: 53px; }
  .divider {
    position: absolute; left: 84px; top: 515px; width: 994px; height: 3px;
    background: var(--accent);
  }
  .contact {
    position: absolute; left: 0; width: 100%; text-align: center;
    font-size: 31px; line-height: 1;
  }
  .contact-address { top: 540px; }
  .contact-web { top: 584px; }
</style>
</head>
<body>
  <div class="card">
    <div class="card-frame"></div>

    <div class="text brand-name">Mavenbrook Holdings</div>
    <div class="brand-mark"></div>

    <div class="text tagline-lead">Turning Old Doors</div>
    <div class="text tagline-strong">Into New</div>
    <div class="text tagline-end">Starts</div>

    <div class="divider"></div>

    <p class="contact contact-address">2738 Fenwick Lane Duluth GA 30418 Office: 678-555-0192</p>
    <p class="contact contact-web">mavenbrookholdingsllc.example</p>
  </div>
</body>
</html>
```